Kalvora Cookbook (Independant Kalvora Consultant - not Kalvora themselves)

Approx 120 page Recipe book, need design created for recipe pages.
each recipe illustrated with full colour photograph (supplied) on opposite page.
To included index, contents page, intro, etc
Cover design also to be suggested.
We must have a professional finish, but with a friendly, family theme.
Reason: Deadline extended because I require further designs, please.

```html
<!DOCTYPE html>
<html lang="en">
<head>
<meta charset="utf-8">
<title>Red Capsicum &amp; Broccoli Salad</title>
<link rel="stylesheet" href="https://fonts.googleapis.com/css2?family=Cabin:wght@400;600;700&display=swap">
<style>
  :root {
    --page: #ffffff;
    --ink: #2b2b2b;
    --title: #1f4a3a;
    --muted: #6b6b6b;
    --accent: #3aa6b9;
    --band: #e3e3e3;
    --rule: #9a9a9a;
    --icon: #d9d9d9;
    --icon-ink: #5a5a5a;
  }
  * { margin: 0; padding: 0; box-sizing: border-box; }
  html, body { width: 1200px; height: 681px; overflow: hidden; background: var(--page); }
  body { font-family: "Cabin", sans-serif; color: var(--ink); }
  .spread { position: relative; width: 1200px; height: 681px; background: var(--page); }

  .photo-page {
    position: absolute; left: 0; top: 0; width: 601px; height: 681px;
    background:
      radial-gradient(ellipse at 45% 62%, #c9873f 0%, #9a7a3a 30%, transparent 60%),
      radial-gradient(ellipse at 80% 15%, #c8322a 0%, transparent 35%),
      radial-gradient(ellipse at 8% 20%, #4c7a2e 0%, transparent 30%),
      linear-gradient(180deg, #dcdfe4 0%, #b9bdb4 30%, #8d8a55 60%, #d8dcd8 100%);
  }
  .spine-tab {
    position: absolute; left: 0; top: 210px; width: 50px; height: 257px;
    background: var(--page);
    display: flex; align-items: center; justify-content: center;
  }
  .spine-tab span {
    transform: rotate(-90deg); white-space: nowrap;
    font-weight: 700; font-size: 12.5px; letter-spacing: 0.2px; color: var(--ink);
  }
  .page-divider { position: absolute; left: 601px; top: 0; width: 1px; height: 681px; background: #8a8a8a; }

  .title-band {
    position: absolute; left: 602px; top: 108px; width: 440px; height: 91px;
    background: var(--band); text-align: center; padding-top: 12px; padding-right: 60px;
  }
  .recipe-title { font-weight: 700; font-size: 22px; line-height: 22px; color: var(--title); }
  .diet-tags { font-weight: 700; font-size: 14px; color: var(--muted); margin-top: 3px; }
  .hero-veg {
    position: absolute; left: 972px; top: 0; width: 228px; height: 216px;
    background:
      radial-gradient(circle at 70% 72%, #e3261f 0%, #d01e18 30%, transparent 48%),
      radial-gradient(circle at 42% 48%, #4f8a2c 0%, #3f7a24 28%, transparent 46%),
      radial-gradient(circle at 35% 20%, #8cc63f 0%, transparent 40%);
  }

  .section-icon { position: absolute; width: 32px; height: 32px; }
  .section-head {
    position: absolute; width: 160px; text-align: center;
    color: var(--accent); font-size: 17px; font-weight: 400; letter-spacing: 0.2px;
  }
  .ingredients { position: absolute; left: 664px; top: 296px; list-style: none; }
  .ingredients li { font-size: 12px; font-weight: 600; line-height: 29px; }
  .column-rule { position: absolute; left: 823px; top: 276px; width: 1px; height: 241px; background: var(--rule); }
  .method { position: absolute; left: 832px; top: 296px; width: 330px; list-style: none; }
  .method li {
    position: relative; padding-left: 9px; font-size: 12px; font-weight: 600; line-height: 15px; margin-bottom: 14px;
  }
  .method li.step::before { content: "•"; position: absolute; left: 0; top: 0; }
  .method li.note { margin-top: -1px; }
  .page-number { position: absolute; left: 892px; top: 648px; font-size: 11px; color: var(--muted); }
</style>
</head>
<body>
<main class="spread">
  <div class="photo-page" role="img" aria-label="Photograph of the red capsicum and broccoli salad in a white bowl, with capsicums and broccoli behind"></div>
  <div class="spine-tab"><span>RED CAPSICUM AND BROCCOLI SALAD</span></div>
  <div class="page-divider"></div>

  <header class="title-band">
    <h1 class="recipe-title">RED CAPSICUM &amp; BROCCOLI<br>SALAD</h1>
    <p class="diet-tags">GF DF EF</p>
  </header>
  <div class="hero-veg" role="img" aria-label="Red capsicums, broccoli and green leaves"></div>

  <svg class="section-icon" style="left:707px;top:246px" viewBox="0 0 32 32" aria-hidden="true">
    <circle cx="16" cy="16" r="16" fill="var(--icon)"/>
    <path d="M11 13 L16 7 L21 13" fill="none" stroke="var(--icon-ink)" stroke-width="1.6"/>
    <path d="M8 13 H24 L22 23 H10 Z" fill="var(--icon-ink)"/>
    <path d="M13 15 V21 M16 15 V21 M19 15 V21" stroke="var(--icon)" stroke-width="1.2"/>
  </svg>
  <h2 class="section-head" style="left:643px;top:276px">INGREDIENT</h2>

  <svg class="section-icon" style="left:972px;top:246px" viewBox="0 0 32 32" aria-hidden="true">
    <circle cx="16" cy="16" r="16" fill="var(--icon)"/>
    <circle cx="12" cy="11" r="3" fill="var(--icon-ink)"/>
    <path d="M8 25 V17 Q8 15 10 15 H14 Q16 15 16 17 V25 Z" fill="var(--icon-ink)"/>
    <path d="M17 15 H25 Q25 11 21 11 Q17 11 17 15 Z" fill="var(--icon-ink)"/>
  </svg>
  <h2 class="section-head" style="left:908px;top:276px">RECIPE</h2>

  <ul class="ingredients">
    <li>3 rashers bacon</li>
    <li>1 red pepper</li>
    <li>½ small red onion</li>
    <li>1 head broccoli</li>
    <li>45g cranberries or sultanas</li>
    <li>30g slivered almonds</li>
    <li>French Dressing</li>
  </ul>

  <div class="column-rule"></div>

  <ul class="method">
    <li class="step">Chop bacon into large pieces. Pan fry until crisp. Place into Kalvora bowl.</li>
    <li class="note">Cut red pepper and onion into pieces and add to bowl.</li>
    <li class="step">Chop for 3 seconds on Speed 4.</li>
    <li class="step">Cut broccoli into florets.&nbsp; Add to bowl with cranberries and almonds.</li>
    <li class="step">Chop 5 seconds, Speed 4 or until chopped to desired size.</li>
    <li class="step">Place in serving bowl and drizzle with dressing.</li>
  </ul>

  <p class="page-number">01</p>
</main>
</body>
</html>
```